Bref créative
Business Card, MS Letterhead Template, Envelopes, & E-mail Signature Template for Investment Firm
None - our logo already has the company name included in it
Simple
Peter Dawes
Managing Partner
436 West Fenwick Ave., Suite 210
Fenwick Falls, NC 27999-0417
PDawes@BrambleRidgeLLP.example
www.BrambleRidgeWealthAdvisoryGroup.example
Looking for:
1) Business Cards
2) MS Word Letterhead Template
3) Envelopes - standard size
4) E-mail Signature Template for Outlook
Thanks in advance for your designs and time!
Uploaded the only AI file I have. It has four separate color variations of our logo. We want to use the main logo, which is the blue and gray one. We do not want to use the black and white ones.
This is our logo AI file. Please use the blue and gray one and not the black and white ones.

```html
<!DOCTYPE html>
<html lang="en">
<head>
<meta charset="utf-8">
<title>Bramble Ridge Wealth Advisory Group — Business Card</title>
<link href="https://fonts.googleapis.com/css2?family=Cinzel:wght@400;500&display=swap" rel="stylesheet">
<style>
  :root {
    --navy: #2c3b8e;
    --navy-deep: #24317a;
    --paper: #ffffff;
    --panel-shade: #eef0f4;
    --ink: #2c3b8e;
    --backdrop: #e9e6e1;
  }
  * { box-sizing: border-box; margin: 0; padding: 0; }
  html, body {
    width: 1200px; height: 902px; overflow: hidden;
    background: var(--backdrop);
  }
  .canvas { position: relative; width: 1200px; height: 902px; }
  .card {
    position: absolute; left: 100px; top: 165px;
    width: 1000px; height: 572px;
    background: var(--navy);
    font-family: "Cinzel", "Times New Roman", serif;
    color: var(--ink);
  }
  .panel {
    position: absolute; left: 22px; right: 22px; top: 22px; bottom: 22px;
    background: linear-gradient(180deg, var(--paper) 0%, var(--panel-shade) 100%);
    border-radius: 14px 44px 44px 14px;
    overflow: hidden;
  }
  .brand {
    position: absolute; left: 40px; top: 120px;
    display: flex; align-items: center; gap: 22px;
  }
  .brand-mark { width: 58px; height: 58px; background: var(--navy); }
  .brand-name {
    font-weight: 400; color: var(--navy);
    text-transform: uppercase; line-height: 1.05;
  }
  .brand-name .primary { display: block; font-size: 50px; letter-spacing: 1px; }
  .brand-name .secondary { display: block; font-size: 22px; letter-spacing: 4px; }
  .name-band {
    position: absolute; left: 0; right: 22px; top: 270px; height: 50px;
    background: var(--navy);
    display: flex; align-items: center; padding-left: 38px;
    color: var(--paper); font-size: 19px; letter-spacing: 1px;
    text-transform: uppercase;
  }
  .name-band .title { margin-left: 10px; }
  .contact {
    position: absolute; left: 40px; top: 352px;
    list-style: none; font-size: 17px; text-transform: uppercase;
    letter-spacing: 0.5px;
  }
  .contact li {
    display: flex; align-items: flex-start; gap: 12px;
    line-height: 22px; margin-bottom: 3px;
  }
  .contact svg { flex: none; margin-top: 2px; }
  .website {
    position: absolute; right: 52px; top: 440px;
    font-size: 15px; text-transform: uppercase; letter-spacing: 0.5px;
  }
</style>
</head>
<body>
<div class="canvas">
  <section class="card" aria-label="Business card for Peter Dawes">
    <div class="panel">
      <div class="brand">
        <span class="brand-mark" aria-hidden="true"></span>
        <span class="brand-name">
          <span class="primary">Bramble Ridge</span>
          <span class="secondary">Wealth Advisory Group</span>
        </span>
      </div>

      <ul class="contact">
        <li>
          <svg width="18" height="18" viewBox="0 0 18 18" aria-hidden="true"><circle cx="9" cy="9" r="9" fill="var(--navy)"/><path d="M9 4a3 3 0 0 1 3 3c0 2.3-3 6-3 6S6 9.3 6 7a3 3 0 0 1 3-3z" fill="#fff"/><circle cx="9" cy="7" r="1.1" fill="var(--navy)"/></svg>
          <span>436 West Fenwick Ave., Suite<br>210 Fenwick Falls, NC 27999-0417</span>
        </li>
        <li>
          <svg width="18" height="18" viewBox="0 0 18 18" aria-hidden="true"><circle cx="9" cy="9" r="9" fill="var(--navy)"/><path d="M6 4.5l2 2-1 1.3c.6 1.3 1.5 2.2 2.8 2.8l1.3-1 2 2-1.2 1.6C8.5 13 5 9.5 4.8 5.7z" fill="#fff"/></svg>
          <span>704-555-0140</span>
        </li>
        <li>
          <svg width="18" height="18" viewBox="0 0 18 18" aria-hidden="true"><circle cx="9" cy="9" r="9" fill="var(--navy)"/><rect x="6.3" y="4" width="5.4" height="10" rx="1" fill="#fff"/><rect x="7.2" y="5.2" width="3.6" height="6" fill="var(--navy)"/></svg>
          <span>704-555-0172</span>
        </li>
        <li>
          <svg width="18" height="18" viewBox="0 0 18 18" aria-hidden="true"><circle cx="9" cy="9" r="9" fill="var(--navy)"/><rect x="4.5" y="7" width="9" height="5" rx="1" fill="#fff"/><rect x="6.5" y="4.5" width="5" height="3" fill="#fff"/></svg>
          <span>704-555-0188</span>
        </li>
        <li>
          <svg width="18" height="18" viewBox="0 0 18 18" aria-hidden="true"><circle cx="9" cy="9" r="9" fill="var(--navy)"/><rect x="4.5" y="5.8" width="9" height="6.4" fill="#fff"/><path d="M4.5 5.8L9 9.5l4.5-3.7" fill="none" stroke="var(--navy)" stroke-width="1"/></svg>
          <span>PDawes@BrambleRidgeLLP.example</span>
        </li>
      </ul>

      <p class="website">www.BrambleRidgeWealthAdvisoryGroup.example</p>
    </div>

    <div class="name-band">
      <span class="name">Peter Dawes</span>
      <span class="title">Managing Partner</span>
    </div>
  </section>
</div>
</body>
</html>
```